Global Expert Network Firm needs business card design

We need business card design for a new company based in Seoul, South Korea called 'Corwell Insight Partners'. We recruit industry experts covering all countries and connect our client and recruited expert by phone, face-to-face meetings and etc. We are a global expert network firm that is focused on delivering high-quality experts to our clients throughout the world. Our clients include multinational corporations, global consulting firms, private equity firms, venture capital firms, asset management companies.
We have made new logo and please find attachment.(Please use new logo)
Target Market(s)
Global Consulting Firms, Investment Firms, Private Equity Firms, Venture Capital Firms.
Industry/Entity Type
Recruitment
Contact Information for Business Card
We need two Languages (English and Korean Version).
The front is Korean and the back is English version.
[The back] [English]
Company Name: Corwell Insight Partners, Inc.
CEO Name: Daniel Park
Address: #507, Hanbit Bldg, 82 Maebongsan-ro, Dobong-gu, Seoul, 01327, Korea
Tel. +82 2 718 4052
Fax. +82 2 864 1097
Mobile. +82 10 7264 8815
Email: daniel@corwellip.com
Web: www.corwellip.com
[The front] [Korean] => Described in same order as English version.
회사명: 코웰인사이트파트너스(주)
대표이사: 박도현
주소: 서울시 도봉구 매봉산로 82 한빛빌딩 507호
Tel. 02 718 4052
Fax. 02 864 1097
Mobile. 010 7264 8815
Web: www.corwellip.com
Look and feel
Each slider illustrates characteristics of the customer's brand and the style your logo design should communicate.

```html
<!DOCTYPE html>
<html lang="en">
<head>
<meta charset="utf-8">
<title>Corwell Insight Partners – Business Cards</title>
<link rel="stylesheet" href="https://fonts.googleapis.com/css2?family=Mulish:wght@300;400;700&family=Noto+Sans+KR:wght@300;400;500&display=swap">
<style>
  :root {
    --backdrop: #2f2522;
    --navy: #1f2868;
    --navy-ink: #1d2459;
    --paper: #f3f3f2;
    --white: #ffffff;
    --soft-white: #d9dcef;
  }
  * { box-sizing: border-box; margin: 0; padding: 0; }
  html, body { width: 1200px; height: 663px; overflow: hidden; }
  body {
    background: var(--backdrop);
    font-family: "Mulish", "Noto Sans KR", sans-serif;
    position: relative;
  }
  .card {
    position: absolute;
    top: 181px;
    width: 540px;
    height: 300px;
    border-radius: 3px;
    box-shadow: 0 8px 24px rgba(0,0,0,.35);
  }
  .card--english { left: 40px; background: var(--navy); color: var(--white); }
  .card--korean { left: 620px; background: var(--paper); color: var(--navy-ink); font-family: "Noto Sans KR", sans-serif; }

  .brand {
    position: absolute;
    top: 48px;
    right: 40px;
    display: flex;
    align-items: center;
    gap: 8px;
    font-family: "Mulish", sans-serif;
    font-weight: 400;
    font-size: 14px;
    letter-spacing: .4px;
    white-space: nowrap;
  }
  .brand__mark {
    width: 10px;
    height: 10px;
    background: currentColor;
    flex: none;
  }

  .identity {
    position: absolute;
    top: 96px;
    right: 312px;
    text-align: right;
  }
  .identity__name { font-size: 21px; line-height: 1.1; }
  .identity__name strong { font-weight: 700; }
  .identity__name span { font-weight: 300; }
  .identity__title { font-size: 9px; font-weight: 400; margin-top: 2px; letter-spacing: .5px; }
  .card--korean .identity__name { font-size: 23px; font-weight: 500; letter-spacing: 2px; }

  .divider {
    position: absolute;
    left: 238px;
    top: 92px;
    width: 1px;
    height: 74px;
    background: currentColor;
    opacity: .85;
  }

  .contact-list {
    position: absolute;
    left: 252px;
    top: 96px;
    list-style: none;
    font-family: "Mulish", sans-serif;
    font-size: 11px;
    font-weight: 400;
    letter-spacing: .4px;
  }
  .card--korean .contact-list { font-size: 12px; }
  .contact-list li { display: flex; align-items: center; gap: 8px; height: 23px; }
  .icon { width: 11px; height: 11px; flex: none; fill: currentColor; }

  .company {
    position: absolute;
    left: 30px;
    top: 176px;
  }
  .company__name { font-size: 10px; font-weight: 700; letter-spacing: .3px; text-transform: uppercase; }
  .company__address { font-size: 8.5px; font-weight: 400; margin-top: 4px; letter-spacing: .2px; color: var(--soft-white); }
  .card--korean .company__name { font-size: 11px; font-weight: 500; text-transform: none; }
  .card--korean .company__address { font-size: 9.5px; color: var(--navy-ink); }

  .online-list {
    position: absolute;
    left: 362px;
    top: 214px;
    list-style: none;
    font-family: "Mulish", sans-serif;
    font-size: 10px;
    font-weight: 400;
  }
  .online-list li { display: flex; align-items: center; gap: 8px; height: 22px; }
</style>
</head>
<body>

<svg width="0" height="0" style="position:absolute" aria-hidden="true">
  <symbol id="icon-phone" viewBox="0 0 12 12"><path d="M2.5 1h2l1 2.5-1.3 1a6 6 0 0 0 3.3 3.3l1-1.3L11 7.5v2a1.2 1.2 0 0 1-1.3 1.2A9 9 0 0 1 1.3 2.3 1.2 1.2 0 0 1 2.5 1z"/></symbol>
  <symbol id="icon-fax" viewBox="0 0 12 12"><path d="M3 1h6v3H3zM1 4.5h10v5H9V8H3v1.5H1zM3 8.5h6V11H3z"/></symbol>
  <symbol id="icon-mobile" viewBox="0 0 12 12"><path d="M3.5 0.5h5a1 1 0 0 1 1 1v9a1 1 0 0 1-1 1h-5a1 1 0 0 1-1-1v-9a1 1 0 0 1 1-1zM3.7 1.7v7.6h4.6V1.7z"/></symbol>
  <symbol id="icon-web" viewBox="0 0 12 12"><path d="M6 .5a5.5 5.5 0 1 0 0 11 5.5 5.5 0 0 0 0-11zm0 1c.6.6 1.1 1.8 1.3 3.3H4.7C4.9 3.3 5.4 2.1 6 1.5zM1.6 5.8h2.1c0 .2 0 .4.1.6l-.1.6H1.6zm3.1 0h2.6v1.2H4.7zm3.6 0h2.1v1.2H8.3zM4.7 8h2.6C7.1 9 6.6 10 6 10.5 5.4 10 4.9 9 4.7 8z"/></symbol>
  <symbol id="icon-at" viewBox="0 0 12 12"><path d="M6 .5a5.5 5.5 0 1 0 3 10.1l-.5-.8A4.5 4.5 0 1 1 10.5 6v.6c0 .7-.4 1.1-.9 1.1s-.9-.4-.9-1.1V3.5h-1v.5A2.5 2.5 0 1 0 7.9 8a1.9 1.9 0 0 0 1.7 1c1.1 0 1.9-.9 1.9-2.2V6A5.5 5.5 0 0 0 6 .5zm0 4a1.5 1.5 0 1 1 0 3 1.5 1.5 0 0 1 0-3z"/></symbol>
</svg>

<article class="card card--english" aria-label="English side of business card">
  <div class="brand"><span class="brand__mark" aria-hidden="true"></span>Corwell Insight Partners</div>

  <div class="identity">
    <p class="identity__name"><strong>Daniel</strong> <span>Park</span></p>
    <p class="identity__title">CEO</p>
  </div>

  <div class="divider"></div>

  <ul class="contact-list">
    <li><svg class="icon"><use href="#icon-phone"/></svg>+82 2 718 4052</li>
    <li><svg class="icon"><use href="#icon-fax"/></svg>+82 2 864 1097</li>
    <li><svg class="icon"><use href="#icon-mobile"/></svg>+82 10 7264 8815</li>
  </ul>

  <div class="company">
    <p class="company__name">Corwell Insight Partners, Inc.</p>
    <p class="company__address">#507, Hanbit Bldg, 82 Maebongsan-ro, Dobong-gu, Seoul, 01327, Korea</p>
  </div>

  <ul class="online-list">
    <li><svg class="icon"><use href="#icon-web"/></svg>www.corwellip.com</li>
    <li><svg class="icon"><use href="#icon-at"/></svg>daniel@corwellip.com</li>
  </ul>
</article>

<article class="card card--korean" lang="ko" aria-label="Korean side of business card">
  <div class="brand" lang="en"><span class="brand__mark" aria-hidden="true"></span>Corwell Insight Partners</div>

  <div class="identity">
    <p class="identity__name">박도현</p>
  </div>

  <div class="divider"></div>

  <ul class="contact-list">
    <li><svg class="icon"><use href="#icon-phone"/></svg>02 718 4052</li>
    <li><svg class="icon"><use href="#icon-fax"/></svg>02 864 1097</li>
    <li><svg class="icon"><use href="#icon-mobile"/></svg>010 7264 8815</li>
  </ul>

  <div class="company">
    <p class="company__name">코웰인사이트파트너스(주)</p>
    <p class="company__address">서울시 도봉구 매봉산로 82 한빛빌딩 507호</p>
  </div>

  <ul class="online-list">
    <li><svg class="icon"><use href="#icon-web"/></svg>www.corwellip.com</li>
    <li><svg class="icon"><use href="#icon-at"/></svg>daniel@corwellip.com</li>
  </ul>
</article>

</body>
</html>
```